We need a business card design for a Dubai based company .

We need a business card for a Dubai based company called "Zernova Trading Co.". We mainly import Flavoured Tobacco products and Charcoal which is used for smoking in a Hookah/Shisha and distribute to the wholesalers and retailers. Logo file is attached herewith.

```html
<!DOCTYPE html>
<html lang="en">
<head>
<meta charset="utf-8">
<title>Zernova Trading Co. – Business Card</title>
<link rel="stylesheet" href="https://fonts.googleapis.com/css2?family=Montserrat:wght@600;700&family=Lato:wght@400&display=swap">
<style>
  :root {
    --backdrop: #222728;
    --card-grey: #dedcdc;
    --card-grey-dark: #bab8b5;
    --card-pink: #e0aba0;
    --card-rose: #cbb7b4;
    --brand-red: #a8393a;
    --brand-black: #232122;
    --text-dark: #1f1d1e;
    --text-light: #fff6f3;
  }
  * { margin: 0; padding: 0; box-sizing: border-box; }
  html, body { width: 1200px; height: 800px; overflow: hidden; }
  body {
    background: var(--backdrop);
    font-family: "Montserrat", sans-serif;
    position: relative;
  }
  .card {
    position: absolute;
    top: 245px;
    width: 540px;
    height: 310px;
    border-radius: 24px;
    overflow: hidden;
    background: var(--card-grey);
  }
  .card--front { left: 40px; }
  .card--back {
    left: 620px;
    background: linear-gradient(90deg, var(--card-grey-dark) 0%, #c6c4c1 45%, var(--card-rose) 55%, #d4c3c1 100%);
  }
  .card__art { position: absolute; inset: 0; width: 100%; height: 100%; }

  .brand {
    position: absolute;
    display: flex;
    align-items: center;
    gap: 10px;
  }
  .brand__mark {
    width: 14px;
    height: 14px;
    background: var(--brand-red);
    flex: none;
  }
  .brand__name {
    font-family: "Montserrat", sans-serif;
    font-weight: 600;
    font-size: 15px;
    letter-spacing: 2px;
    text-transform: uppercase;
    color: var(--text-dark);
    white-space: nowrap;
  }
  .card--front .brand { left: 62px; top: 146px; }

  .holder { position: absolute; left: 300px; top: 62px; }
  .holder__name {
    font-weight: 700;
    font-size: 21px;
    letter-spacing: 0.5px;
    color: var(--text-dark);
  }
  .holder__name span { color: var(--brand-red); }
  .holder__role {
    font-weight: 600;
    font-size: 17px;
    color: var(--text-dark);
    margin-top: 2px;
  }
  .holder__role span { color: var(--brand-red); }

  .contacts {
    position: absolute;
    left: 300px;
    top: 172px;
    list-style: none;
  }
  .contacts__item {
    display: flex;
    align-items: center;
    gap: 14px;
    height: 25px;
    font-family: "Lato", sans-serif;
    font-size: 12.5px;
    color: var(--text-light);
  }
  .contacts__icon { width: 22px; height: 20px; flex: none; }

  .emblem-panel {
    position: absolute;
    left: 175px;
    top: 60px;
    width: 190px;
    height: 190px;
    background: #d6d3d2;
    border: 10px solid #e6e4e3;
    display: flex;
    align-items: center;
    justify-content: center;
  }
  .emblem-panel .brand { position: static; }
  .emblem-panel .brand__name { font-size: 13px; letter-spacing: 1.5px; }
</style>
</head>
<body>

<section class="card card--front" aria-label="Business card front">
  <svg class="card__art" viewBox="0 0 540 310" preserveAspectRatio="none" aria-hidden="true">
    <polygon points="262,0 540,0 540,310 300,310" fill="var(--card-pink)"/>
    <polygon points="0,0 150,0 0,52" fill="var(--brand-black)"/>
    <polygon points="150,0 175,0 0,62 0,52" fill="var(--brand-red)"/>
    <polygon points="0,310 0,296 240,264 240,276 10,310" fill="var(--brand-red)" opacity="0"/>
    <polygon points="90,310 270,258 270,270 130,310" fill="var(--brand-black)"/>
    <polygon points="130,310 270,270 270,280 165,310" fill="var(--brand-red)"/>
  </svg>

  <div class="brand">
    <span class="brand__mark"></span>
    <p class="brand__name">Zernova Trading Co.</p>
  </div>

  <div class="holder">
    <h1 class="holder__name">DANIEL <span>REYES</span></h1>
    <p class="holder__role"><span>Your</span> Designation</p>
  </div>

  <ul class="contacts">
    <li class="contacts__item">
      <svg class="contacts__icon" viewBox="0 0 22 20" aria-hidden="true"><polygon points="6,1 16,1 21,10 16,19 6,19 1,10" fill="var(--brand-red)" stroke="#fff" stroke-width="1.2"/><path d="M8 7 q0 6 6 6 l1-2 -2-1 -1 1 q-2-1 -3-3 l1-1 -1-2z" fill="#fff"/></svg>
      +000 12345 6789
    </li>
    <li class="contacts__item">
      <svg class="contacts__icon" viewBox="0 0 22 20" aria-hidden="true"><polygon points="6,1 16,1 21,10 16,19 6,19 1,10" fill="var(--brand-red)" stroke="#fff" stroke-width="1.2"/><rect x="7" y="7" width="8" height="6" fill="#fff"/><path d="M7 7 l4 3 4-3" stroke="var(--brand-red)" fill="none"/></svg>
      info@yourmail.com
    </li>
    <li class="contacts__item">
      <svg class="contacts__icon" viewBox="0 0 22 20" aria-hidden="true"><polygon points="6,1 16,1 21,10 16,19 6,19 1,10" fill="var(--brand-red)" stroke="#fff" stroke-width="1.2"/><circle cx="11" cy="10" r="4" fill="none" stroke="#fff"/><path d="M7 10 h8 M11 6 v8" stroke="#fff"/></svg>
      www.yourwebsite.com
    </li>
    <li class="contacts__item">
      <svg class="contacts__icon" viewBox="0 0 22 20" aria-hidden="true"><polygon points="6,1 16,1 21,10 16,19 6,19 1,10" fill="var(--brand-red)" stroke="#fff" stroke-width="1.2"/><path d="M11 15 l-3-5 a3.5 3.5 0 1 1 6 0z" fill="#fff"/><circle cx="11" cy="8.5" r="1.2" fill="var(--brand-red)"/></svg>
      your address here
    </li>
  </ul>
</section>

<section class="card card--back" aria-label="Business card back">
  <svg class="card__art" viewBox="0 0 540 310" preserveAspectRatio="none" aria-hidden="true">
    <polygon points="0,0 120,0 0,42" fill="var(--brand-black)"/>
    <polygon points="120,0 145,0 0,52 0,42" fill="var(--brand-red)"/>
    <polygon points="540,310 400,310 540,262" fill="var(--brand-black)"/>
    <polygon points="400,310 375,310 540,252 540,262" fill="var(--brand-red)"/>
  </svg>

  <div class="emblem-panel">
    <div class="brand">
      <span class="brand__mark"></span>
      <p class="brand__name">Zernova<br>Trading Co.</p>
    </div>
  </div>
</section>

</body>
</html>
```